Book cover needed for Christian Non-Fiction Book

I need book cover design (eBook , Paperback, and possibly case laminate Hardcover) for use on Folvane Press and Corvel Print.
Title: Bound for Shore
Sub-Title: Leaving Harbors and Walking in Quiet Trust
Author: Neil Varden
Also on front cover "Forward by R. Leona Pask"

I like clean/simple designs. Below are links to examples of covers I like...
https://www.shelvora.example/dp/Q4821MZT0X?tag=kelvpage-20&linkCode=ogi&th=1&psc=1
https://www.shelvora.example/dp/Q48HTRNWAC?tag=kelvpage-20&linkCode=ogi&th=1&psc=1
https://www.shelvora.example/dp/Q22FKD93XJ?tag=kelvpage-20&linkCode=ogi&th=1&psc=1
https://www.shelvora.example/dp/Q48W3PLMHD?tag=kelvpage-20&linkCode=ogi&th=1&psc=1
https://www.shelvora.example/dp/Q48R5ZZCQN?tag=kelvpage-20&linkCode=ogi&th=1&psc=1
https://www.shelvora.example/dp/Q22H0KKPU7?tag=kelvpage-20&linkCode=ogi&th=1&psc=1

The main idea for Bound for Shore is that God is a sending God and being "on the move" or journeying is central to God's character, and therefore God's people. I write about our hesitancy to "go," and how the Bible is full of stories about people "going" from Abraham to Jesus, to the disciples of Jesus.

The core biblical text is the Great Commission in Matthew 28:16-20, where Jesus sends out his followers, though some of them doubt.

This paragraph from the forward by R. Leona Pask captures the tone of the book well:
This book is a call amid the turmoil. Sacred scripture contains no shortage of narratives in which humans are pulled from their ordinary lives with an inciting incident whose stakes are high. These Biblical figures are lulled from complacency and comfort zones—and yet they are reluctant to serve because they question their ability and influence. Their lessons are relevant for us today: They, and we, are always called and sent with authority. The power of the Holy Spirit equips their “going”—and ours. It’s a sending out that looks less like mastery and more humility. It’s a sending out that is unequivocal service to others modelled in a rabbi-reformer who washed feet and touched the unclean.

I have previously published two shorter books and would be very interested in getting new covers for the old books these so that the three have a similar feel. Whichever designer I go with for "Bound for Shore" I would also want to work with on creating a "branded look" for the other two books.

Target Market(s)

Christian, Religion, Spirituality Readers

Requirements
Must have
• The front cover must have this copy...
Bound for Shore
Leaving Harbors and Walking in Quiet Trust
Neil Varden
Forward by R. Leona Pask

Must be willing to do the full paperback and/or hardcover, but start with thefront cover please
Nice to have
• See attached files for some book covers I like

```html
<!DOCTYPE html>
<html lang="en">
<head>
<meta charset="utf-8">
<title>Bound for Shore — Front Cover</title>
<link rel="stylesheet" href="https://fonts.googleapis.com/css2?family=Libre+Baskerville:wght@400;700&family=Source+Sans+3:ital,wght@0,600;0,700;1,400&display=swap">
<style>
  :root {
    --page-bg: #ffffff;
    --sky-top: #07b6cc;
    --sky-mid: #1cc6d6;
    --sky-horizon: #3fd3dc;
    --field-light: #f0c372;
    --field-mid: #e2a84f;
    --field-deep: #c98a3a;
    --title-mint: #93e6c6;
    --text-white: #ffffff;
    --cover-shadow: rgba(0, 0, 0, 0.28);
  }
  html, body {
    margin: 0;
    padding: 0;
    width: 1200px;
    height: 1000px;
    overflow: hidden;
    background: var(--page-bg);
  }
  .canvas {
    position: relative;
    width: 1200px;
    height: 1000px;
  }
  .cover {
    position: absolute;
    left: 288px;
    top: 28px;
    width: 627px;
    height: 944px;
    overflow: hidden;
    box-shadow: 2px 3px 6px var(--cover-shadow);
  }
  .cover-photo {
    position: absolute;
    inset: 0;
    background:
      radial-gradient(circle at 61% 45%, rgba(220, 255, 230, 0.75) 0, rgba(140, 235, 215, 0.35) 60px, rgba(60, 210, 215, 0) 170px),
      linear-gradient(to bottom,
        var(--sky-top) 0%,
        var(--sky-mid) 40%,
        var(--sky-horizon) 65%,
        var(--field-light) 65.4%,
        var(--field-mid) 82%,
        var(--field-deep) 100%);
  }
  .cover-type {
    position: absolute;
    left: 74px;
    width: 430px;
    top: 0;
  }
  .book-title {
    position: absolute;
    top: 146px;
    left: -20px;
    width: 470px;
    margin: 0;
    text-align: center;
    font-family: "Libre Baskerville", Georgia, serif;
    font-weight: 400;
    font-size: 45px;
    letter-spacing: 0.5px;
    line-height: 1;
    color: var(--title-mint);
    white-space: nowrap;
  }
  .book-subtitle {
    position: absolute;
    top: 202px;
    left: -20px;
    width: 470px;
    margin: 0;
    text-align: center;
    font-family: "Libre Baskerville", Georgia, serif;
    font-weight: 700;
    font-size: 15.5px;
    line-height: 1;
    color: var(--text-white);
    white-space: nowrap;
  }
  .byline {
    position: absolute;
    top: 312px;
    right: 0;
    text-align: right;
    font-family: "Source Sans 3", "Helvetica Neue", Arial, sans-serif;
    color: var(--text-white);
  }
  .author-name {
    margin: 0;
    font-weight: 600;
    font-size: 22px;
    line-height: 24px;
    letter-spacing: 0.3px;
    text-transform: uppercase;
  }
  .foreword-credit {
    margin: 1px 0 0;
    font-size: 15px;
    line-height: 18px;
  }
  .foreword-credit .label {
    font-style: italic;
    font-weight: 400;
  }
  .foreword-credit .name {
    font-weight: 700;
    text-transform: uppercase;
    letter-spacing: 0.3px;
  }
</style>
</head>
<body>
<div class="canvas">
  <section class="cover">
    <div class="cover-photo" role="img" aria-label="Photograph of a man walking away through a golden wheat field under a bright turquoise sky, with a soft sun glow above him"></div>
    <div class="cover-type">
      <h1 class="book-title">BOUND FOR SHORE</h1>
      <p class="book-subtitle">Leaving Harbors and Walking in Quiet Trust</p>
      <div class="byline">
        <p class="author-name">Neil Varden</p>
        <p class="foreword-credit"><span class="label">Forward by</span> <span class="name">R. Leona Pask</span></p>
      </div>
    </div>
  </section>
</div>
</body>
</html>
```